Counting Toward Purpose institute for nonprofits needs brochure

The Counting Toward Purpose performance management institute helps nonprofits clarify the intended impact of their programs on clients. What does a nonprofit want to accomplish - and what does it need to measure so that it can tell if they've achieved impact? The Institute is about to recruit participanting organizations. We have a lot of wording on a 2 page "flyer" that describes the institute...but it is a very ugly piece that looks unprofessional. We are looking for designs that are consistent with the KRT Advisory Group look (see our website). We are aware that we may have too much wording.

Target Market(s)

Nonprofit organization Executive Directors

Industry/Entity Type

Non-Profit

Font styles to use
Sans Serif

Requirements
Must have
• Must be able to be emailed to a client and printed on 8.5x11 paper. Doesn't matter to me if that makes it a tri-fold or two-fold.
• Need to be able to drop in later the actual dates of the program.
• Go to our website to see how we present ourselves. www.krtadvisoryhub.example
Nice to have
• See our website for KRT Advisory's "look". Our colors are green and gray (in the logo), with complementary colors of blue and orange.
• Looking for creativity in the graphics design. Our two page document has way too many words. The word impact is very important to the concept of performance management (and I'm not sure it's in the 2 page write up) - so you could do something with that word if you wanted to.
• Could use Davina's pic if it makes sense.
Should not have
• No new logo for the Counting Toward Purpose institute. It should be clear that KRT Advisory Group is the entity that offers the institute.

```html
<!DOCTYPE html>
<html lang="en">
<head>
<meta charset="utf-8">
<title>KRT Advisory – Counting Toward Purpose Institute Brochure</title>
<link rel="stylesheet" href="https://fonts.googleapis.com/css2?family=Montserrat:wght@600;700;800&family=Open+Sans:ital,wght@0,300;0,400;0,600;0,700;1,400;1,600&display=swap">
<style>
  :root {
    --green: #8cc63f;
    --green-dark: #5e9423;
    --gray: #6d6e71;
    --gray-dark: #4d4e50;
    --gray-light: #d5d6d8;
    --paper: #ffffff;
    --stage: #ececec;
    --ink: #3c3d3f;
  }
  * { box-sizing: border-box; margin: 0; padding: 0; }
  html, body { width: 1200px; height: 800px; overflow: hidden; }
  body {
    background: var(--stage);
    font-family: "Open Sans", Arial, sans-serif;
    color: var(--ink);
    position: relative;
  }
  .spread {
    position: absolute;
    left: 100px; top: 75px;
    width: 1000px; height: 650px;
    display: flex;
    box-shadow: 0 6px 24px rgba(0,0,0,.18);
  }
  .page {
    position: relative;
    width: 500px; height: 650px;
    background: var(--paper);
    overflow: hidden;
  }
  .page svg.shapes { position: absolute; left: 0; display: block; }

  /* ---------- Inside page: About ---------- */
  .about-head {
    position: absolute; left: 40px; top: 78px;
    width: 170px; height: 28px;
    background: var(--green-dark);
    color: #fff;
    font-family: "Montserrat", Arial, sans-serif;
    font-weight: 700; font-size: 13px; letter-spacing: 3px;
    display: flex; align-items: center; justify-content: center;
  }
  .about-body {
    position: absolute; left: 40px; top: 120px; width: 420px;
    font-size: 10px; line-height: 1.5; color: var(--gray-dark);
  }
  .about-body p + p { margin-top: 7px; }
  .about-body strong { font-weight: 700; color: var(--ink); }
  .program-dates { font-weight: 700; color: var(--green-dark); }
  .about-mark {
    position: absolute; left: 0; right: 0; top: 292px;
    text-align: center;
    font-weight: 300; font-size: 26px; color: #9a9b9e; letter-spacing: .5px;
  }
  .about-photo {
    position: absolute; left: 0; top: 340px; width: 500px; height: 220px;
    background: linear-gradient(180deg, #ffffff 0%, #e6e7e8 45%, #d2d3d5 100%);
    opacity: .8;
  }
  .contact-band {
    position: absolute; left: 0; bottom: 0; width: 500px; height: 92px;
    background: var(--green);
    display: flex; gap: 34px;
    padding: 20px 0 0 40px;
    color: #fff; font-size: 9.5px; line-height: 1.5;
  }
  .contact-item { display: flex; gap: 8px; align-items: flex-start; }
  .contact-item svg { flex: none; margin-top: 2px; }
  .contact-col { display: flex; flex-direction: column; gap: 6px; }

  /* ---------- Cover page ---------- */
  .cover-photo {
    position: absolute; left: 0; top: 0; width: 500px; height: 340px;
    background: linear-gradient(135deg, #c9d2da 0%, #8fa3b5 40%, #b7a79a 70%, #e4ddd6 100%);
  }
  .cover-brand {
    position: absolute; left: 0; right: 0; top: 385px;
    text-align: center;
    font-weight: 300; font-size: 38px; color: var(--gray); letter-spacing: .5px;
  }
  .cover-title {
    position: absolute; left: 0; right: 0; top: 448px; text-align: center;
    font-family: "Montserrat", Arial, sans-serif; font-weight: 800;
    font-size: 44px; color: var(--green); letter-spacing: 2px; line-height: 1;
  }
  .cover-subtitle {
    position: absolute; left: 0; right: 0; top: 500px; text-align: center;
    font-family: "Montserrat", Arial, sans-serif; font-weight: 700;
    font-size: 21px; color: var(--gray); letter-spacing: 1.5px;
  }
  .cover-tagline {
    position: absolute; left: 0; right: 0; top: 530px; text-align: center;
    font-style: italic; font-weight: 600; font-size: 11px; color: var(--gray-dark);
  }
  .cover-rule {
    position: absolute; left: 0; top: 576px; width: 500px; height: 5px;
    background: var(--green);
  }
  .cover-web {
    position: absolute; left: 0; top: 588px; width: 500px; height: 38px;
    background: var(--gray);
    color: #fff; font-weight: 600; font-size: 15px; letter-spacing: 2.5px;
    display: flex; align-items: center; justify-content: center;
  }
</style>
</head>
<body>
<main class="spread">

  <section class="page page-about">
    <svg class="shapes" style="top:0" width="500" height="75" viewBox="0 0 500 75" aria-hidden="true">
      <path d="M0 0 H500 V18 C360 8 200 22 0 62 Z" fill="var(--gray-light)"/>
      <path d="M0 0 H500 V6 C360 -2 190 12 0 44 Z" fill="var(--green)"/>
      <path d="M0 0 H500 V2 C360 -6 190 4 0 28 Z" fill="var(--gray)"/>
    </svg>

    <h2 class="about-head">ABOUT US</h2>

    <div class="about-body">
      <p>Founded in 2002, KRT Advisory helps nonprofits build organizational strength. The Counting Toward Purpose institute is where <strong>Impact Makes the Difference.</strong></p>
      <p>The institute helps Executive Directors clarify the impact their programs should have on clients: what to accomplish, what to measure, and how to tell when impact is achieved. Program dates: <span class="program-dates">Session dates to be announced.</span></p>
      <p>At KRT we are passionate about the value of nonprofit organizations, about their work to touch and change lives, enrich our communities and protect our environment.</p>
    </div>

    <div class="about-mark">KRT Advisory</div>

    <div class="about-photo" role="img" aria-label="Faded portrait photograph of a consultant"></div>

    <svg class="shapes" style="top:518px" width="500" height="50" viewBox="0 0 500 50" aria-hidden="true">
      <path d="M0 50 V36 C160 10 330 6 500 26 V50 Z" fill="var(--green-dark)"/>
      <path d="M0 50 V44 C160 20 330 16 500 34 V50 Z" fill="var(--green)"/>
    </svg>

    <footer class="contact-band">
      <div class="contact-item">
        <svg width="12" height="12" viewBox="0 0 12 12" aria-hidden="true"><path d="M6 1 L11 5.5 H9.5 V11 H7 V8 H5 V11 H2.5 V5.5 H1 Z" fill="#fff"/></svg>
        <div>2480 Alder Creek Road<br>Fenwick, MO 63190<br>17 Larkmoor Lane<br>Brisbow, MO 63195</div>
      </div>
      <div class="contact-col">
        <div class="contact-item">
          <svg width="12" height="12" viewBox="0 0 12 12" aria-hidden="true"><path d="M2.5 1 L4.5 1 L5.5 3.5 L4.2 4.6 C4.9 6 6 7.1 7.4 7.8 L8.5 6.5 L11 7.5 V9.5 C11 10.3 10.3 11 9.5 11 C5 11 1 7 1 2.5 C1 1.7 1.7 1 2.5 1 Z" fill="#fff"/></svg>
          <span>314-555-0148</span>
        </div>
        <div class="contact-item">
          <svg width="12" height="12" viewBox="0 0 12 12" aria-hidden="true"><rect x="1" y="2.5" width="10" height="7" fill="#fff"/><path d="M1 2.5 L6 6.5 L11 2.5" fill="none" stroke="var(--green)" stroke-width="1"/></svg>
          <span>info@krtadvisoryhub.example</span>
        </div>
      </div>
    </footer>
  </section>

  <section class="page page-cover">
    <div class="cover-photo" role="img" aria-label="Photograph of two smiling colleagues talking at a table in a bright office"></div>

    <svg class="shapes" style="top:0" width="500" height="120" viewBox="0 0 500 120" aria-hidden="true">
      <path d="M0 0 H70 C40 30 20 70 0 120 Z" fill="#fff"/>
      <path d="M70 0 H82 C50 30 25 75 0 120 V120 C20 70 40 30 70 0 Z" fill="var(--gray)"/>
      <path d="M82 0 H88 C55 30 28 75 0 120 C25 75 50 30 82 0 Z" fill="var(--green)"/>
    </svg>

    <svg class="shapes" style="top:240px" width="500" height="130" viewBox="0 0 500 130" aria-hidden="true">
      <path d="M0 40 C120 120 330 110 500 30 V130 H0 Z" fill="var(--gray)"/>
      <path d="M0 62 C130 132 330 120 500 48 V130 H0 Z" fill="var(--green)"/>
      <path d="M0 76 C130 140 330 130 500 62 V130 H0 Z" fill="var(--gray-light)"/>
      <path d="M0 86 C130 148 330 140 500 74 V130 H0 Z" fill="#fff"/>
    </svg>

    <div class="cover-brand">KRT Advisory</div>
    <h1 class="cover-title">BUILDING</h1>
    <p class="cover-subtitle">ORGANIZATION STRENGTH</p>
    <p class="cover-tagline">Consulting with nonprofits to build successful organizations.</p>
    <div class="cover-rule"></div>
    <div class="cover-web">www.krtadvisoryhub.example</div>
  </section>

</main>
</body>
</html>
```